light box menu and wall graphics

HI My name is Derek Vantolla and I am putting together a Pebble Wagons franchise. We are a high quaulity coffee offering and the retail concept is for a in-line store in a busy shopping centre food court. We are a highly visible coffee offering with vibrant bright orange colour (pantone 021 / process m60_y100)
Orange might make a good background on the menu board as it needs to blend in with colour scheme. Also the text has to be at least 15ml and not too busy but clearly legible. The font is: Akzent Rounded
The twin light boxes being used is from http://www.brightframedepot.com.au/pg/lightboxes/new/sdb/light-box-2270K.aspx
They measure in total 3m wide X .6 height

There are two elements to this job, one is the twin menu boards and the other is the wall graphic.
please see wall graphic examples attached.
This graphic is to be painted onto the wall by a sign writter.
The design to go on the wall needs to be a synonymous with our quality coffee vison and match the shop design, I have examples of the type of wall art I am after attached. I was thinking somehow a Cart with wings would look neat and we could incorportate some text into it. Such as "Coffee with Substance makes you feel good" and "Genuine Wagon" Flames could look amazing too!

My website is unfortunately down at the moment but I am attaching plenty

I have just added the menu in easy to read updated format.
Thanks to those who have expressed interest!
Updates

Hi Designers, I have just increased first prize by $100.00

Please note the signage boards run horizontally not vertically.  I have also added more artwork.

thanks

Derek

 HI there, thanks for joining.  I have just updated the brief to make it as clear as possible.

Hope you enjoy this experience.  I am here to answer any questions.

Derek

Thank you for accepting my invitation for this design job.

Look forward to seeing some designs as per brief.

Need to have this finished by Friday the 19th of October.  Thanks

Target Market(s)

Coffee lovers, kids who want hot chocolates, frappes,
etc

Industry/Entity Type

Shopping

Requirements
Must have
• Must have coffee in it for clarity.
Also in the menu any images of food or drink must be photo/posters attached

```html
<!DOCTYPE html>
<html lang="en">
<head>
<meta charset="utf-8">
<title>Coffee Menu Board</title>
<link rel="stylesheet" href="https://fonts.googleapis.com/css2?family=Arimo:wght@700&display=swap">
<style>
  :root {
    --board-orange: #e97e22;
    --peach: #f9d3b0;
    --ink: #0d0a06;
    --rule-brown: #8b4a12;
    --divider: #f6d9bf;
  }
  html, body {
    margin: 0;
    padding: 0;
    width: 1200px;
    height: 599px;
    overflow: hidden;
    background: var(--board-orange);
  }
  .menu-board {
    position: relative;
    width: 1200px;
    height: 599px;
    background: var(--board-orange);
    font-family: "Arimo", "Helvetica Neue", Arial, sans-serif;
    font-weight: 700;
    line-height: 1;
    overflow: hidden;
  }
  .menu-board > * { position: absolute; margin: 0; white-space: nowrap; }

  .header-rule { top: 128px; height: 8px; background: var(--rule-brown); }
  .header-rule--left { left: 0; width: 452px; }
  .header-rule--right { left: 460px; right: 0; }
  .column-divider { top: 0; left: 452px; width: 8px; height: 599px; background: var(--divider); }

  .section-title { left: 72px; top: 34px; font-size: 76px; color: var(--peach); letter-spacing: -0.5px; -webkit-text-stroke: 1px var(--peach); }

  .size-price { top: 40px; font-size: 46px; color: var(--ink); letter-spacing: -0.5px; -webkit-text-stroke: 0.8px var(--ink); }
  .size-price .amount { color: var(--peach); -webkit-text-stroke: 0.8px var(--peach); }
  .size-shots { top: 95px; font-size: 28px; color: var(--peach); }

  .drink-list { left: 74px; top: 0; padding: 0; list-style: none; }
  .drink-item { position: absolute; left: 0; font-size: 49px; color: var(--ink); letter-spacing: -0.6px; -webkit-text-stroke: 0.8px var(--ink); }

  .extras-list { left: 589px; top: 0; padding: 0; list-style: none; }
  .extra { position: absolute; left: 0; font-size: 27px; color: var(--peach); letter-spacing: -0.2px; }
  .extra .mark { color: var(--ink); }
  .extra .bullet { color: var(--ink); font-size: 22px; vertical-align: 2px; margin-right: 6px; }
  .extra .note { font-size: 21px; }
  .extra .flavours { font-size: 19px; }
</style>
</head>
<body>
<main class="menu-board">
  <h1 class="section-title">Coffee</h1>

  <p class="size-price" style="left:544px">S $<span class="amount">3.80</span></p>
  <p class="size-price" style="left:729px">M $<span class="amount">4.50</span></p>
  <p class="size-price" style="left:922px">L $<span class="amount">4.90</span></p>
  <p class="size-shots" style="left:546px">(1 Shot)</p>
  <p class="size-shots" style="left:731px">(2 Shot)</p>
  <p class="size-shots" style="left:927px">(2 Shot)</p>

  <div class="header-rule header-rule--left"></div>
  <div class="header-rule header-rule--right"></div>
  <div class="column-divider"></div>

  <ul class="drink-list">
    <li class="drink-item" style="top:162px">Espresso Shot</li>
    <li class="drink-item" style="top:228px">Long Black</li>
    <li class="drink-item" style="top:293px">Flat White</li>
    <li class="drink-item" style="top:357px">Latte</li>
    <li class="drink-item" style="top:421px">Cappuccino</li>
    <li class="drink-item" style="top:485px">Hot Chocolate</li>
  </ul>

  <ul class="extras-list">
    <li class="extra" style="top:159px"><span class="mark">$</span> 2.90</li>
    <li class="extra" style="top:198px"><span class="mark">+</span> 50¢</li>
    <li class="extra" style="top:236px"><span class="bullet">•</span>Soy</li>
    <li class="extra" style="top:275px"><span class="bullet">•</span>Mocha</li>
    <li class="extra" style="top:313px"><span class="bullet">•</span>Vienna</li>
    <li class="extra" style="top:351px"><span class="bullet">•</span>Decaf <span class="note">(fresh)</span></li>
    <li class="extra" style="top:389px"><span class="bullet">•</span>Syrups; <span class="flavours">vanilla, caramel, hazelnut</span></li>
    <li class="extra" style="top:427px"><span class="bullet">•</span>Cream</li>
    <li class="extra" style="top:466px"><span class="bullet">•</span>Coffee shot</li>
    <li class="extra" style="top:504px"><span class="bullet">•</span>White chocolate</li>
  </ul>
</main>
</body>
</html>
```